Website for Private Psychologist

DO NOT CONTACT ME PRIVATELY

I am a Psychologist offering psychotherapy for individuals and couples, and clinical consultation and training and education for mental and medical health professionals and agencies.

I need a redesign of my website

5 Pages (content is attached for each page)
Home
Jungian Psychotherapy
Clinical Consultation & Professional Development
Curriculum Vitae & Publications
Practice Policies and Forms

Designs can be based on these style websites
https://lqmindcare.info; https://pdtarn.org/; https://dorabellcroftcounselling.com/

Design Concepts
Minimalist Layout: Clean and uncluttered layout with generous white space, allowing the content and visuals to stand out'

Keep a linear, uncluttered, professional design.

Please use only royalty free images and google fonts. Please provide links to any stock images used to verify license.

Target Market(s)

private individual or couples seeking psychotherapy

Industry/Entity Type

Psychotherapy

Number of Pages Required

5+ page

Requirements
Should not have
• No search feature

```html
<!DOCTYPE html>
<html lang="en">
<head>
<meta charset="utf-8">
<title>Martin Aldecott, Psy.D</title>
<link href="https://fonts.googleapis.com/css2?family=Poppins:wght@400;500;600&family=Josefin+Sans:wght@300;400&display=swap" rel="stylesheet">
<style>
:root{
  --green:#5a9a4f;
  --ink:#2d2d2d;
  --text:#4a4a4a;
  --hero-bg:#eff8fa;
  --soft:#f7f7f7;
  --label-bg:#f3f3f3;
  --white:#ffffff;
}
*{box-sizing:border-box;margin:0;padding:0}
html,body{width:1200px;height:2601px;overflow:hidden}
body{font-family:"Josefin Sans",sans-serif;font-weight:300;color:var(--text);background:var(--white);position:relative}
.abs{position:absolute}
.heading{font-family:"Poppins",sans-serif;color:var(--ink);font-weight:600}

.site-header{position:absolute;left:0;top:0;width:1200px;height:115px;background:var(--white)}
.brand-name{left:110px;top:28px;font-size:25px}
.brand-sub{left:110px;top:72px;font-size:15px;color:var(--text);font-weight:400}
.main-nav a{position:absolute;top:29px;font-family:"Poppins",sans-serif;font-size:15.5px;line-height:20.5px;color:#444;text-decoration:none}

.hero{position:absolute;left:0;top:115px;width:1200px;height:583px;background:var(--hero-bg)}
.hero-title{left:110px;top:88px;font-size:35px}
.hero-sub{left:110px;top:144px;font-family:"Poppins",sans-serif;font-size:20px;color:var(--green);font-weight:500}
.hero-text{left:110px;top:202px;width:445px;font-size:17.5px;line-height:25px}
.hero-call{left:110px;top:373px;font-size:17.5px}
.contact-line{left:110px;font-size:19px;color:#333;font-weight:400;display:flex;align-items:center;gap:6px}
.hero-photo{left:617px;top:40px;width:490px;height:490px;border-radius:50%;background:radial-gradient(circle at 45% 40%,#c79a72,#6e5444 60%,#202020);box-shadow:0 10px 30px rgba(0,0,0,.12)}

.approach{position:absolute;left:0;top:698px;width:1200px;height:528px}
.office-a{left:111px;top:77px;width:229px;height:318px;background:linear-gradient(160deg,#d9dbe0,#8a8e97 55%,#3d4458)}
.service-label{left:352px;top:77px;width:245px;height:112px;background:var(--label-bg);padding:20px 24px;font-family:"Poppins",sans-serif;font-size:20px;line-height:24px;color:var(--green);font-weight:500}
.office-b{left:352px;top:202px;width:245px;height:195px;background:linear-gradient(120deg,#e4e0da,#8b6a4a 55%,#3f3630)}
.approach-title{left:676px;top:62px;font-size:42px}
.approach-text{left:678px;top:150px;width:418px;font-size:17.5px;line-height:25.7px}
.btn-green{left:678px;top:394px;width:158px;height:53px;border-radius:27px;background:var(--green);color:var(--white);font-family:"Poppins",sans-serif;font-weight:500;font-size:17px;display:flex;align-items:center;justify-content:center}

.offering{position:absolute;left:0;top:1226px;width:1200px;height:595px;background:var(--soft)}
.offering-title{left:0;width:1200px;top:70px;text-align:center;font-size:40px}
.card{position:absolute;top:171px;width:313px}
.card-img{height:298px}
.card-cap{margin-top:22px;text-align:center;font-family:"Poppins",sans-serif;font-weight:500;font-size:21px;color:var(--ink)}

.contact{position:absolute;left:0;top:1821px;width:1200px;height:502px;background:var(--green);color:var(--white)}
.contact-title{left:0;width:1200px;top:50px;text-align:center;font-size:42px;color:var(--white)}
.contact-info{left:0;width:1200px;top:122px;display:flex;justify-content:center;align-items:center;gap:12px;font-size:21px;font-weight:400}
.field{position:absolute;border:1px solid rgba(255,255,255,.85);font-size:18px;padding:12px 20px;color:var(--white);font-weight:400}
.btn-white{left:535px;top:384px;width:130px;height:55px;border-radius:28px;background:var(--white);color:var(--ink);font-family:"Poppins",sans-serif;font-weight:500;font-size:17px;display:flex;align-items:center;justify-content:center}

.site-footer{position:absolute;left:0;top:2323px;width:1200px;height:278px}
.social{position:absolute;top:67px;width:41px;height:41px;border:1px solid var(--green);border-radius:50%}
.footer-links{left:0;width:1200px;text-align:center;font-size:18px;color:#444;line-height:28px}
.copyright{left:0;width:1200px;top:210px;text-align:center;font-size:17px;color:#444}
</style>
</head>
<body>

<header class="site-header">
  <div class="abs heading brand-name">Martin Aldecott, Psy.D</div>
  <div class="abs brand-sub">California Licensed Psychologist PSY 48150</div>
  <nav class="main-nav">
    <a style="left:493px">Jungian<br>Psychotherapy</a>
    <a style="left:633px">Clinical Consultation<br>&amp; Professional<br>Development</a>
    <a style="left:814px">Curriculum Vitae<br>&amp; Publications</a>
    <a style="left:967px">Practice Policies<br>and Forms</a>
  </nav>
</header>

<section class="hero">
  <h1 class="abs heading hero-title">Martin Aldecott, Psy.D.</h1>
  <div class="abs hero-sub">California Licensed Psychologist PSY 48150</div>
  <p class="abs hero-text">I am a California Licensed Psychologist with an office in the San Francisco Financial District offering psychotherapy for individuals and couples, and clinical consultation and training and education for mental and medical health professionals and agencies. All appointments are currently available via telehealth.</p>
  <p class="abs hero-call">For an initial consultation please call:</p>
  <div class="abs contact-line" style="top:420px">
    <svg width="17" height="17" viewBox="0 0 24 24"><path fill="#5a9a4f" d="M6.6 10.8a15.1 15.1 0 006.6 6.6l2.2-2.2a1 1 0 011-.25 11.4 11.4 0 003.6.57 1 1 0 011 1V20a1 1 0 01-1 1A17 17 0 013 4a1 1 0 011-1h3.5a1 1 0 011 1c0 1.25.2 2.45.57 3.57a1 1 0 01-.25 1z"/></svg>
    <span>(415) 555-0182</span><span style="font-size:17px;margin-left:8px;font-weight:300">or</span>
  </div>
  <div class="abs contact-line" style="top:453px">
    <svg width="20" height="16" viewBox="0 0 24 18"><rect width="24" height="18" rx="2" fill="#5a9a4f"/><path d="M2 3l10 7 10-7" stroke="#fff" stroke-width="2" fill="none"/></svg>
    <span>maldecott@quietmail.net</span>
  </div>
  <div class="abs hero-photo" role="img" aria-label="Portrait photograph of the psychologist"></div>
</section>

<section class="approach">
  <div class="abs office-a" role="img" aria-label="Photograph of the therapy office with window and armchair"></div>
  <div class="abs service-label">Clinical Consultation &amp; Professional Development</div>
  <div class="abs office-b" role="img" aria-label="Photograph of the office desk and bookshelf"></div>
  <h2 class="abs heading approach-title">My Approach</h2>
  <p class="abs approach-text">I provide professional consultation for pre- and post-licensed psychotherapists on a range of clinical issues including substance use disorder assessment and treatment; motivational interviewing; and treatment issues specific to LGBT clients. For Psychology Interns and trainees I offer clinical supervision, case consultation, and professional development.</p>
  <div class="abs btn-green">READ MORE</div>
</section>

<section class="offering">
  <h2 class="abs heading offering-title">Offering Psychotherapy For</h2>
  <div class="card" style="left:111px">
    <div class="card-img" role="img" aria-label="Photograph of a therapy session with clasped hands" style="background:linear-gradient(135deg,#d8dcdf,#6f7a86 50%,#2c3a55)"></div>
    <div class="card-cap">Individuals and couples</div>
  </div>
  <div class="card" style="left:444px">
    <div class="card-img" role="img" aria-label="Photograph of a clinician writing on a clipboard" style="background:linear-gradient(135deg,#f1e6dc,#dfe3e8 50%,#6e7388)"></div>
    <div class="card-cap">Clinical consultation</div>
  </div>
  <div class="card" style="left:776px">
    <div class="card-img" role="img" aria-label="Photograph of a group of smiling healthcare professionals" style="background:linear-gradient(135deg,#cfc1b2,#a8b9c8 55%,#5e7ea0)"></div>
    <div class="card-cap">Training and education</div>
  </div>
</section>

<section class="contact">
  <h2 class="abs heading contact-title">Contact Me</h2>
  <div class="abs contact-info">
    <svg width="18" height="18" viewBox="0 0 24 24"><path fill="#fff" d="M6.6 10.8a15.1 15.1 0 006.6 6.6l2.2-2.2a1 1 0 011-.25 11.4 11.4 0 003.6.57 1 1 0 011 1V20a1 1 0 01-1 1A17 17 0 013 4a1 1 0 011-1h3.5a1 1 0 011 1c0 1.25.2 2.45.57 3.57a1 1 0 01-.25 1z"/></svg>
    <span>(415) 555-0182</span><span style="margin:0 8px">|</span>
    <svg width="21" height="16" viewBox="0 0 24 18"><rect width="24" height="18" rx="2" fill="#fff"/><path d="M2 3l10 7 10-7" stroke="#5a9a4f" stroke-width="2" fill="none"/></svg>
    <span>maldecott@quietmail.net</span>
  </div>
  <div class="field" style="left:181px;top:194px;width:415px;height:48px">Name</div>
  <div class="field" style="left:181px;top:252px;width:415px;height:48px">Email</div>
  <div class="field" style="left:181px;top:311px;width:415px;height:48px">Phone No</div>
  <div class="field" style="left:605px;top:194px;width:415px;height:166px">Message</div>
  <div class="abs btn-white">SUBMIT</div>
</section>

<footer class="site-footer">
  <span class="social" style="left:532px" aria-label="Social profile"></span>
  <span class="social" style="left:580px" aria-label="Social profile"></span>
  <span class="social" style="left:628px" aria-label="Social profile"></span>
  <div class="abs footer-links" style="top:130px">Home &nbsp;|&nbsp; Jungian Psychotherapy &nbsp;|&nbsp; Clinical Consultation &amp; Professional Development</div>
  <div class="abs footer-links" style="top:158px">| &nbsp;Curriculum Vitae &amp; Publications &nbsp;|&nbsp; Practice Policies and Forms</div>
  <div class="abs copyright">2023 © Martin Aldecott, Psy.D.</div>
</footer>

</body>
</html>
```